velumora.eu :: Design ideas (no coding) for key pages of Personalized greeting cards online store

We need your vision on modern, clean, easy to read user interface (UI) for online service of personalized printed products, like greeting cards, postcards, fridge magnets, clips and etc.
Your vision should include UI presentation for:
- Home page with login (including soc nets)
- Product Designer page
- Cart pages (products and address selection)
- Example of general internal page (pricing, terms, etc)
- Artist info and portfolio page
We are looking for ideas we will love, NOT complete design of a whole site.
Top design/vision will we used as a basement for separate contract on complete design of the site.

UI should be based on existing functionality with some extent. It should not break ideas or methods used on prototype but designers are free to offer own product presentations, designer’s layout and cart views.

Prototype:
English: http://velumora.eu
Russian: http://velumora.ru
Lithuanian: http://velumora.lt

Target Market(s)

People of 16-45 y.o. who likes to be distinctive, personal.

Industry/Entity Type

Store

Requirements
Must have
• Your work should meet attached requirements.
Site is multilingual. Wording should assume varieties in length on different languages.
Clean and easy to read UI
Flat design preferrably
Should be based on assets which are free or available for royalty-free licensing
Should not have
• heavy, meaningless 3D and shadow effects
Show NOT copy sites like: kindlow.com, tarnbell.co.uk

```html
<!DOCTYPE html>
<html lang="en">
<head>
<meta charset="utf-8">
<title>velumora — greeting cards</title>
<link href="https://fonts.googleapis.com/css2?family=Ubuntu:wght@300;400;500;700&display=swap" rel="stylesheet">
<style>
:root{
  --red:#a1231b;
  --red-dark:#8a1c15;
  --bg:#f4f3f1;
  --panel:#ffffff;
  --line:#e2e0dc;
  --text:#333;
  --muted:#777;
  --price:#2a8a8a;
  --icon:#9a9a9a;
}
*{box-sizing:border-box;margin:0;padding:0}
html,body{width:1034px;height:1200px;overflow:hidden;background:var(--bg)}
body{font-family:"Ubuntu",sans-serif;color:var(--text)}
.page{position:relative;width:1250px;height:1450px;transform:scale(.8272);transform-origin:0 0}
.abs{position:absolute}

/* header */
.brand{left:115px;top:14px;width:140px;display:flex;flex-direction:column;align-items:center;gap:8px}
.brand-mark{width:60px;height:60px;background:var(--red)}
.brand-name{font-size:24px;font-weight:400;color:var(--red);letter-spacing:.5px}
.tagline{left:0;width:1195px;top:48px;text-align:center;font-size:18px;color:var(--red)}
.tabs{left:267px;top:98px;display:flex;height:36px}
.tab{padding:0 18px;font-size:13px;font-weight:700;line-height:40px;color:#333}
.tab.is-active{background:var(--red);color:#fff;border-radius:4px 4px 0 0}
.account{right:113px;top:107px;display:flex;align-items:center;gap:10px;font-size:13px;font-weight:500;color:#666}
.account .sep{width:1px;height:12px;background:#ccc}
.account b{color:var(--red)}
.rule{left:115px;top:134px;width:1020px;height:3px;background:var(--red)}

/* category bar */
.catbar{left:115px;top:137px;width:1020px;height:94px;background:var(--panel);display:flex;border-bottom:1px solid var(--line)}
.cat{display:flex;align-items:center;gap:14px;font-size:15px;color:#333;border-right:1px solid var(--line);padding:0 22px}
.cat-all{width:151px;background:var(--red);color:#fff;justify-content:center}
.cat-greeting{width:264px;padding-left:34px}
.cat-sound{width:209px;padding-left:32px}
.cat-post{width:214px;padding-left:32px}
.cat-fav{flex:1;border-right:0}
.fav-square{width:36px;height:32px;background:var(--red)}

/* hero */
.hero{left:115px;top:231px;width:1020px;height:249px;background:linear-gradient(100deg,#d9c4ae 0%,#c9ae92 35%,#b89676 60%,#8f7a6a 85%,#5c5a55 100%)}
.hero-caption{left:115px;top:307px;width:320px;height:112px;background:rgba(120,100,85,.75);border-radius:0 4px 4px 0;padding:10px 24px}
.hero-caption h1{font-size:28px;font-weight:700;color:#fff}
.hero-caption p{font-size:22px;font-weight:300;color:#fff;margin-top:-2px}
.btn{display:inline-block;background:var(--red);color:#fff;font-size:13px;border-radius:3px;padding:4px 13px}
.hero-caption .btn{margin-top:6px}

/* sidebar */
.box{background:var(--panel);border:1px solid var(--line)}
.box h2{font-size:18px;font-weight:500;padding:10px 18px;border-bottom:1px solid #f0eee9;height:41px}
.themes{left:115px;top:493px;width:261px;height:429px}
.tags{display:flex;flex-wrap:wrap;gap:6px 6px;padding:14px 14px 0 16px}
.tag{border:1px solid var(--line);border-radius:3px;padding:0 12px;height:29px;line-height:27px;font-size:13px;background:#fff}
.tag.lg{font-size:15px;font-weight:500}
.t-black{color:#111;font-weight:700}.t-blue{color:#1c6fb8}.t-orange{color:#e8a21c}.t-brown{color:#b06a2c}
.t-green{color:#3f7d1d}.t-red{color:#b5261c}.t-teal{color:#2a8a8a}.t-purple{color:#a31ca3}.t-olive{color:#8a6f2a}.t-crimson{color:#c8102e}.t-amber{color:#e35d0a}
.colors{left:115px;top:933px;width:261px;height:162px}
.swatches{margin:12px 17px 0;border:2px solid #ddd;height:52px;display:flex;padding:3px}
.swatches span{flex:1}
.colors .btn{margin:16px 0 0 19px}

/* product cards */
.card{background:var(--panel);border:1px solid var(--line)}
.card .art{height:235px}
.card-foot{display:flex;align-items:center;height:58px;padding:0 16px}
.card-foot .price{font-size:15px;font-weight:500;color:var(--price);flex:1}
.card-foot svg{margin-left:8px}
.more{left:585px;top:1420px;width:81px;height:27px;background:var(--red);border-radius:3px;color:#fff;font-size:14px;font-weight:700;display:flex;align-items:center;justify-content:center;gap:6px}
</style>
</head>
<body>
<div class="page">

  <header>
    <div class="abs brand"><span class="brand-mark"></span><span class="brand-name">velumora</span></div>
    <p class="abs tagline">The individual greeting cards according to your mood</p>
    <nav class="abs tabs"><span class="tab is-active">PRODUCTS</span><span class="tab">AUTHORS</span></nav>
    <div class="abs account">
      <svg width="11" height="12" viewBox="0 0 11 12"><circle cx="5.5" cy="3" r="3" fill="#a1231b"/><path d="M0 12c0-4 2.5-5 5.5-5S11 8 11 12z" fill="#a1231b"/></svg>
      <span>SIGN IN</span><span class="sep"></span>
      <svg width="20" height="14" viewBox="0 0 20 14"><path d="M0 1h4l2 8h11l2-6H6" fill="none" stroke="#a1231b" stroke-width="2"/><path d="M5 3h14l-2 6H6z" fill="#a1231b"/><circle cx="8" cy="12" r="1.6" fill="#a1231b"/><circle cx="15" cy="12" r="1.6" fill="#a1231b"/></svg>
      <span><b>CART:</b> 0 ITEMS - $0.00</span>
    </div>
    <div class="abs rule"></div>
  </header>

  <nav class="abs catbar">
    <div class="cat cat-all">
      <svg width="38" height="38" viewBox="0 0 38 38" stroke="#fff" stroke-width="5" stroke-linecap="round"><path d="M19 3v32M5 11l28 16M33 11L5 27"/></svg>All
    </div>
    <div class="cat cat-greeting">
      <svg width="76" height="46" viewBox="0 0 76 46" fill="none" stroke="#a1231b"><rect x="1" y="8" width="26" height="36" fill="#fff"/><path d="M1 8l14-7v8" /><rect x="33" y="17" width="38" height="27" fill="#fff"/><path d="M71 44l4-6-4-6"/></svg>Greeting cards
    </div>
    <div class="cat cat-sound">
      <svg width="40" height="38" viewBox="0 0 40 38" fill="none" stroke="#a1231b" stroke-width="1.3"><path d="M2 13h7l10-9v30l-10-9H2z"/><path d="M24 12c3 4 3 10 0 14M28 8c5 6 5 16 0 22M32 4c7 8 7 22 0 30"/></svg>Sound cards
    </div>
    <div class="cat cat-post">
      <svg width="72" height="42" viewBox="0 0 72 42" fill="none" stroke="#a1231b"><rect x="1" y="1" width="26" height="40"/><rect x="32" y="13" width="39" height="28"/></svg>Postcards
    </div>
    <div class="cat cat-fav"><span class="fav-square"></span>Favorites (1)</div>
  </nav>

  <section class="abs hero" role="img" aria-label="Hand-drawn holiday greeting cards spread across a table"></section>
  <div class="abs hero-caption">
    <h1>Loretm Ipsum Doller</h1>
    <p>Lorem Ipsum Doller</p>
    <span class="btn">CHOOSE SIZE</span>
  </div>

  <aside>
    <section class="abs box themes">
      <h2>Themes</h2>
      <div class="tags">
        <span class="tag t-black">All</span><span class="tag t-blue">Bears</span><span class="tag t-orange">Birthday</span><span class="tag t-brown">Cat</span>
        <span class="tag lg t-green">Cards</span><span class="tag t-red">Christmas</span><span class="tag t-blue">Dogs</span>
        <span class="tag t-teal">Congratulations!</span><span class="tag lg t-blue">Flowers</span>
        <span class="tag t-blue">For children</span><span class="tag lg t-olive">Friendship</span>
        <span class="tag lg t-crimson">Love</span><span class="tag t-purple">Newborn</span><span class="tag lg t-red">Photos</span>
        <span class="tag t-amber">Religion</span><span class="tag lg t-crimson">Valentine's day</span>
        <span class="tag t-blue">For children</span><span class="tag lg t-olive">Friendship</span>
        <span class="tag lg t-crimson">Love</span><span class="tag t-purple">Newborn</span><span class="tag lg t-red">Photos</span>
        <span class="tag t-teal">Congratulations!</span><span class="tag lg t-blue">Flowers</span>
        <span class="tag t-blue">For children</span><span class="tag lg t-olive">Friendship</span>
      </div>
    </section>
    <section class="abs box colors">
      <h2>Colors</h2>
      <div class="swatches"><span style="background:#e6d8b4"></span><span style="background:#c8c8c8"></span></div>
      <span class="btn">Reset to All</span>
    </section>
  </aside>

  <svg width="0" height="0" style="position:absolute">
    <defs>
      <symbol id="i-sound" viewBox="0 0 18 14"><path d="M1 5h3l4-4v12L4 9H1z" fill="none" stroke="#9a9a9a" stroke-width="1.3"/><path d="M11 4c1.5 2 1.5 4 0 6M14 2c3 3 3 7 0 10" fill="none" stroke="#9a9a9a" stroke-width="1.3"/></symbol>
      <symbol id="i-fav" viewBox="0 0 16 15"><path d="M1 14V6l7-5 7 5v8z" fill="none" stroke="#9a9a9a" stroke-width="1.5"/></symbol>
    </defs>
  </svg>

  <main>
    <article class="abs card" style="left:389px;top:494px;width:238px;height:295px">
      <div class="art" role="img" aria-label="Four painted Christmas tree and star tiles on blue" style="background:linear-gradient(135deg,#1f44b8,#e8731c 50%,#1f3fa8)"></div>
      <div class="card-foot"><span class="price">€ 2.99</span><svg width="18" height="14"><use href="#i-sound"/></svg><svg width="16" height="15"><use href="#i-fav"/></svg></div>
    </article>
    <article class="abs card" style="left:644px;top:494px;width:238px;height:295px">
      <div class="art" role="img" aria-label="Patchwork illustration with a white teddy bear" style="background:linear-gradient(135deg,#d9e6ef,#c2d6e8 50%,#efe6d4)"></div>
      <div class="card-foot"><span class="price">€ 0.99</span><svg width="18" height="14"><use href="#i-sound"/></svg><svg width="16" height="15"><use href="#i-fav"/></svg></div>
    </article>
    <article class="abs card" style="left:896px;top:494px;width:238px;height:295px">
      <div class="art" role="img" aria-label="Bouquet of white flowers and pine cones on red" style="background:radial-gradient(circle,#e9e0c8 0%,#8aa352 45%,#c02a22 75%)"></div>
      <div class="card-foot"><span class="price">€ 0.99</span><svg width="18" height="14"><use href="#i-sound"/></svg><svg width="16" height="15"><use href="#i-fav"/></svg></div>
    </article>

    <article class="abs card" style="left:389px;top:801px;width:238px;height:294px">
      <div class="art" role="img" aria-label="Painted nativity scene" style="background:linear-gradient(135deg,#6d7fa8,#b0463a 50%,#d8b47a)"></div>
      <div class="card-foot"><span class="price">€ 2.99</span><svg width="18" height="14"><use href="#i-sound"/></svg><svg width="16" height="15"><use href="#i-fav"/></svg></div>
    </article>
    <article class="abs card" style="left:644px;top:801px;width:238px;height:294px">
      <div class="art" role="img" aria-label="Black and white photo of two monkeys" style="background:linear-gradient(135deg,#9a9a9a,#4c4c4c 50%,#d8d8d8)"></div>
      <div class="card-foot"><span class="price">€ 0.99</span><svg width="18" height="14"><use href="#i-sound"/></svg><svg width="16" height="15"><use href="#i-fav"/></svg></div>
    </article>
    <article class="abs card" style="left:896px;top:801px;width:238px;height:294px">
      <div class="art" role="img" aria-label="Child with teddy bear under a smiling sun" style="background:linear-gradient(180deg,#f7c531 0%,#e4f0f7 45%,#f0d9e6)"></div>
      <div class="card-foot"><span class="price">€ 0.99</span><svg width="18" height="14"><use href="#i-sound"/></svg><svg width="16" height="15"><use href="#i-fav"/></svg></div>
    </article>

    <article class="abs card" style="left:115px;top:1115px;width:259px;height:284px">
      <div class="art" role="img" aria-label="Photo of assorted seashells" style="margin:0 11px;height:229px;background:linear-gradient(135deg,#c9a684,#7a5a48 50%,#e0cdb0)"></div>
      <div class="card-foot"><span class="price">€ 0.99</span><svg width="16" height="15"><use href="#i-fav"/></svg></div>
    </article>
    <article class="abs card" style="left:389px;top:1115px;width:238px;height:284px">
      <div class="art" role="img" aria-label="Child in a cap under a smiling sun" style="height:232px;background:linear-gradient(180deg,#f6c02c 0%,#e6f2f8 50%,#f2c9d3)"></div>
      <div class="card-foot"><span class="price">€ 0.99</span><svg width="16" height="15"><use href="#i-fav"/></svg></div>
    </article>
    <article class="abs card" style="left:644px;top:1115px;width:239px;height:284px">
      <div class="art" role="img" aria-label="Four tiles: heart, bouquet, glasses and rings" style="height:232px;background:linear-gradient(135deg,#c47ad8,#8dd646 45%,#f0b838 60%,#d6231c)"></div>
      <div class="card-foot"><span class="price">€ 0.99</span><svg width="16" height="15"><use href="#i-fav"/></svg></div>
    </article>
    <article class="abs card" style="left:896px;top:1115px;width:239px;height:284px">
      <div class="art" role="img" aria-label="Flowers in a pot on a dotted blue background" style="height:232px;background:radial-gradient(circle,#d6352a 0%,#e8a62a 25%,#3c3fd8 60%)"></div>
      <div class="card-foot"><span class="price">€ 0.99</span><svg width="16" height="15"><use href="#i-fav"/></svg></div>
    </article>
  </main>

  <div class="abs more"><svg width="12" height="8" viewBox="0 0 12 8"><path d="M1 1l5 5 5-5" fill="none" stroke="#fff" stroke-width="2"/></svg>MORE</div>
</div>
</body>
</html>
```